6 page A4 trifold flyer/ brochure

We need an A4 flyer/brochure folding into 3 making 6 pages to advertise our Children Farm Park, we are looking for a CLEAR easy to understand bright fun exciting look
I have included a lot of photos and images we do not require all to be used

our strap line A Fun filled day on the farm

Details

Highlight all activities included in entry price

the services we offer

Indoor play
photo 5 488
photo 7 2797
photo 24 1090898 laser
photo 17 & 18 go karts

Animal Petting
We have over 200 animals
Seasonally we customers can bottle feed lambs (file 1 quillmere lamb)
Bottle feed calves, handle Ducklings, chicks, Rabbits, guinea Pigs, Ferrets

Meet the farm animals on our Tractor train ride (file 9 )

animal files file 2 044
file 13 14 15 16

Outdoor play
inflatables file 6
Peddle carts file 8
Go Carts file 4
Play Village file 10
play Castle file 19
Crazy golf
Fairy lake file

we do SHows special events/days during the year
Pirate Day file 12
Knights and dragon show file 11
other shows Wild west, fairy and Pixie, Prince and Princess,
Christmas file 25 and 26
Halloween file 27
we also have characters file 20 21 22 23 who the 4 quillmere acres is based on

Cafe Serving hot/cold Food and drinks open all day

Company details
telephone number 01847 530214
www.quillmere-acres.com
address Quillmere Acres Ashcombe road, Fernleigh, Hampshire, RG27 4QT

Open 10am - 6.30pm Easter summer Autumn
10am - 5pm Winter

Prices Adult £8.95 Child £7.95 Under 2`s Free Concessions £6.95
Family of 4 only £29.95

Map

please add

subject to Terms and Conditions see our website

all activities are subject to availability and weather

```html
<!DOCTYPE html>
<html lang="en">
<head>
<meta charset="utf-8">
<title>Quillmere Acres – Trifold Flyer</title>
<link rel="stylesheet" href="https://fonts.googleapis.com/css2?family=Bubblegum+Sans&family=Comfortaa:wght@400;700&display=swap">
<style>
  :root {
    --sky: #3ba9e0;
    --sky-light: #5cc2ee;
    --green: #5cb531;
    --lime: #a6d13a;
    --navy: #1d3f8f;
    --white: #ffffff;
    --page-bg: #eef1f4;
  }
  html, body {
    margin: 0;
    width: 1200px;
    height: 850px;
    overflow: hidden;
    background: var(--page-bg);
  }
  .flyer { width: 1200px; height: 850px; }
  .side { display: flex; width: 1200px; height: 425px; }
  .panel {
    position: relative;
    width: 400px;
    height: 425px;
    overflow: hidden;
    background: var(--sky);
    box-sizing: border-box;
  }
  .photo { position: absolute; }

  /* Shared slanted heading band */
  .band { position: absolute; left: -6px; width: 412px; height: 34px; }
  .band svg { display: block; }
  .band__title {
    position: absolute; inset: 0;
    display: flex; align-items: center; justify-content: center;
    font-family: "Bubblegum Sans", sans-serif;
    font-size: 22px;
    letter-spacing: 5px;
    text-transform: uppercase;
    color: var(--white);
    text-shadow: 1px 2px 0 rgba(0,0,0,0.35);
  }

  /* Panel: activities */
  .hours {
    position: absolute; left: 0; top: 0;
    width: 400px; height: 36px;
    display: flex; flex-direction: column; align-items: center; justify-content: center;
    color: var(--white);
    font-family: "Comfortaa", sans-serif;
    font-size: 10px; font-weight: 700; line-height: 1.35;
    text-align: center;
  }
  .photo--playground { left: 0; top: 36px; width: 400px; height: 104px;
    background: linear-gradient(160deg, #7a9a5c 0%, #b48b5a 45%, #8f6a42 75%, #5d7d3b 100%); }
  .band--indoor { top: 132px; }
  .photo--indoor-a { left: 0; top: 166px; width: 180px; height: 92px;
    background: linear-gradient(150deg, #c98a64 0%, #d9a7c2 50%, #7c5b4a 100%); }
  .photo--indoor-b { left: 184px; top: 166px; width: 216px; height: 92px;
    background: linear-gradient(150deg, #3c3a52 0%, #e0c437 40%, #b13a3a 70%, #2f2c3d 100%); }
  .band--outdoor { top: 256px; }
  .photo--outdoor-a { left: 0; top: 290px; width: 160px; height: 100px;
    background: linear-gradient(160deg, #2e8fd0 0%, #5fbf4a 55%, #2e7a3a 100%); }
  .photo--outdoor-b { left: 164px; top: 290px; width: 236px; height: 100px;
    background: linear-gradient(160deg, #6e8fb0 0%, #e9e4dc 40%, #c9394a 65%, #3f5a2f 100%); }
  .strip-meet {
    position: absolute; left: 0; top: 390px;
    width: 400px; height: 35px;
    background: var(--lime);
    display: flex; align-items: center; justify-content: center;
    font-family: "Bubblegum Sans", sans-serif;
    font-size: 16px; letter-spacing: 1px;
    color: var(--navy);
  }

  /* Panel: prices and contact */
  .prices {
    position: absolute; left: 0; top: 0;
    width: 400px; height: 138px;
    padding: 14px 44px 0;
    box-sizing: border-box;
    font-family: "Comfortaa", sans-serif;
    color: var(--white);
  }
  .prices__row {
    display: flex; justify-content: space-between;
    font-size: 15px; font-weight: 700; line-height: 1.62;
  }
  .photo--goat { left: 0; top: 138px; width: 400px; height: 150px;
    background: linear-gradient(150deg, #6fa6c9 0%, #d8d2c4 45%, #9b8a6e 75%, #4d6a33 100%); }
  .divider { position: absolute; left: 0; top: 288px; width: 400px; height: 8px; background: var(--green); }
  .contact {
    position: absolute; left: 0; top: 296px;
    width: 400px; height: 129px;
    padding: 14px 40px 0;
    box-sizing: border-box;
    font-family: "Comfortaa", sans-serif;
    font-size: 13px; font-weight: 700;
    color: var(--white);
  }
  .contact__row { display: flex; align-items: center; gap: 10px; margin-bottom: 9px; line-height: 1.35; }
  .contact__icon { flex: none; width: 18px; height: 18px; }

  /* Panel: cover */
  .panel--cover { background: var(--sky-light); }
  .cover__edge { position: absolute; left: 0; top: 0; width: 10px; height: 425px; background: var(--lime); }
  .brand {
    position: absolute; right: 20px; top: 14px;
    display: flex; align-items: center; gap: 8px;
    font-family: "Bubblegum Sans", sans-serif;
    font-size: 17px;
    color: var(--navy);
  }
  .brand__dot { width: 14px; height: 14px; border-radius: 50%; background: var(--navy); }
  .cover__title {
    position: absolute; left: 10px; top: 48px;
    width: 390px; margin: 0;
    text-align: center;
    font-family: "Bubblegum Sans", sans-serif;
    font-weight: 400; font-size: 24px; line-height: 1.1;
    color: var(--navy);
  }
  .cover__scene {
    position: absolute; left: 10px; top: 110px;
    width: 390px; height: 225px;
    background: linear-gradient(180deg, #8fd6f5 0%, #c9c1d8 30%, #d85a55 45%, #e8d4a8 60%, #7cc242 78%, #4e9a2c 100%);
  }
  .cover__footer {
    position: absolute; left: 10px; top: 335px;
    width: 390px; height: 90px; margin: 0;
    background: var(--green);
    padding: 16px 30px;
    box-sizing: border-box;
    font-family: "Comfortaa", sans-serif;
    font-size: 11px; line-height: 1.6;
    color: var(--white);
    text-align: center;
  }

  /* Inside panels */
  .panel--inside { padding-top: 48px; }
  .panel--inside .band { top: 8px; }
  .inside__photos { display: flex; gap: 4px; height: 150px; }
  .inside__photos .photo { position: static; flex: 1; }
  .inside__text {
    padding: 14px 28px 0;
    font-family: "Comfortaa", sans-serif;
    font-size: 12px; font-weight: 700; line-height: 1.6;
    color: var(--white);
  }
  .inside__lead {
    margin: 0 0 6px;
    font-family: "Bubblegum Sans", sans-serif;
    font-weight: 400; font-size: 19px; line-height: 1.2;
    color: var(--navy);
  }
  .inside__text p { margin: 0 0 6px; }
  .photo--lamb { background: linear-gradient(150deg, #e8e2d4 0%, #bfae92 50%, #6d8d3e 100%); }
  .photo--calf { background: linear-gradient(150deg, #9c7a5a 0%, #e5d8c4 45%, #5f8a3a 100%); }
  .photo--pirate { background: linear-gradient(150deg, #2c3e5a 0%, #c9a26a 50%, #8a2f2f 100%); }
  .photo--knight { background: linear-gradient(150deg, #8a9aa8 0%, #d9d2c0 45%, #4f7a34 100%); }
  .panel--cafe { background: var(--green); }
  .photo--cafe { background: linear-gradient(150deg, #d8b48a 0%, #f0e3cf 50%, #9a6a44 100%); }
  .map {
    margin: 10px 28px 0;
    height: 92px;
    background: linear-gradient(135deg, #d8e9c4 0%, #b9d89a 60%, #9cc4e0 100%);
  }
  .terms {
    margin: 8px 28px 0;
    font-family: "Comfortaa", sans-serif;
    font-size: 10px; font-weight: 700; line-height: 1.5;
    color: var(--white);
  }
</style>
</head>
<body>
<main class="flyer">

  <div class="side side--outside">
    <section class="panel panel--activities">
      <div class="hours">
        <span>Open :</span>
        <span>10am - 6.30pm (easter,summer,autumn) &amp; 10am - 5pm (winter)</span>
      </div>
      <div class="photo photo--playground" role="img" aria-label="Photo of the wooden outdoor play village"></div>
      <div class="band band--indoor">
        <svg width="412" height="34" viewBox="0 0 412 34" aria-hidden="true"><polygon points="0,8 412,0 412,26 0,34" fill="var(--green)"/></svg>
        <span class="band__title">Indoor Play</span>
      </div>
      <div class="photo photo--indoor-a" role="img" aria-label="Photo of a girl playing on the indoor spinner"></div>
      <div class="photo photo--indoor-b" role="img" aria-label="Photo of children driving indoor go karts"></div>
      <div class="band band--outdoor">
        <svg width="412" height="34" viewBox="0 0 412 34" aria-hidden="true"><polygon points="0,0 412,8 412,34 0,26" fill="var(--lime)"/></svg>
        <span class="band__title">Outdoor Play</span>
      </div>
      <div class="photo photo--outdoor-a" role="img" aria-label="Photo of children on the inflatables"></div>
      <div class="photo photo--outdoor-b" role="img" aria-label="Photo of a costumed farm character in the play village"></div>
      <div class="strip-meet">Meet the farm animals on our tractor train ride</div>
    </section>

    <section class="panel panel--prices">
      <div class="prices">
        <div class="prices__row"><span>Adult</span><span>£8.95</span></div>
        <div class="prices__row"><span>Child</span><span>£7.95</span></div>
        <div class="prices__row"><span>Concessions</span><span>£6.95</span></div>
        <div class="prices__row"><span>Family of 4 only</span><span>£29.95</span></div>
        <div class="prices__row"><span>Under 2's</span><span>Free</span></div>
      </div>
      <div class="photo photo--goat" role="img" aria-label="Photo of a goat beside the windmill"></div>
      <div class="divider"></div>
      <div class="contact">
        <div class="contact__row">
          <svg class="contact__icon" viewBox="0 0 24 24" aria-hidden="true"><path fill="var(--white)" d="M6.6 10.8a15 15 0 0 0 6.6 6.6l2.2-2.2c.3-.3.7-.4 1-.2 1.1.4 2.3.6 3.6.6.6 0 1 .4 1 1V20c0 .6-.4 1-1 1A17 17 0 0 1 3 4c0-.6.4-1 1-1h3.5c.6 0 1 .4 1 1 0 1.3.2 2.5.6 3.6.1.3 0 .7-.2 1z"/></svg>
          <span>01847 530214</span>
        </div>
        <div class="contact__row">
          <svg class="contact__icon" viewBox="0 0 24 24" aria-hidden="true"><circle cx="12" cy="12" r="9" fill="none" stroke="var(--white)" stroke-width="2"/><path d="M3 12h18M12 3c3 3 3 15 0 18M12 3c-3 3-3 15 0 18" fill="none" stroke="var(--white)" stroke-width="1.6"/></svg>
          <span>www.quillmere-acres.com</span>
        </div>
        <div class="contact__row">
          <svg class="contact__icon" viewBox="0 0 24 24" aria-hidden="true"><path fill="var(--white)" d="M12 2a7 7 0 0 0-7 7c0 5 7 13 7 13s7-8 7-13a7 7 0 0 0-7-7zm0 9.5A2.5 2.5 0 1 1 12 6.5a2.5 2.5 0 0 1 0 5z"/></svg>
          <span>Quillmere Acres, Ashcombe road, Fernleigh, Hampshire, RG27 4QT</span>
        </div>
      </div>
    </section>

    <section class="panel panel--cover">
      <div class="cover__edge"></div>
      <div class="brand"><span class="brand__dot"></span><span>Quillmere Acres</span></div>
      <h1 class="cover__title">A family fun filled Day out<br>on the farm</h1>
      <div class="cover__scene" role="img" aria-label="Illustration of a castle, two children and farm animals in a green meadow"></div>
      <p class="cover__footer">All outdoor activities are subject to weather conditions. Our Chatterpost page is regularly updated with all the great things to see and do.</p>
    </section>
  </div>

  <div class="side side--inside">
    <section class="panel panel--inside panel--animals">
      <div class="band">
        <svg width="412" height="34" viewBox="0 0 412 34" aria-hidden="true"><polygon points="0,8 412,0 412,26 0,34" fill="var(--green)"/></svg>
        <span class="band__title">Animal Petting</span>
      </div>
      <div class="inside__photos">
        <div class="photo photo--lamb" role="img" aria-label="Photo of a child bottle feeding a lamb"></div>
        <div class="photo photo--calf" role="img" aria-label="Photo of calves and rabbits at the farm"></div>
      </div>
      <div class="inside__text">
        <h2 class="inside__lead">We have over 200 animals!</h2>
        <p>Seasonally you can bottle feed lambs and calves, and handle ducklings, chicks, rabbits, guinea pigs and ferrets.</p>
        <p>Meet the farm animals on our tractor train ride.</p>
      </div>
    </section>

    <section class="panel panel--inside panel--shows">
      <div class="band">
        <svg width="412" height="34" viewBox="0 0 412 34" aria-hidden="true"><polygon points="0,0 412,8 412,34 0,26" fill="var(--lime)"/></svg>
        <span class="band__title">Shows &amp; Events</span>
      </div>
      <div class="inside__photos">
        <div class="photo photo--pirate" role="img" aria-label="Photo from the pirate day show"></div>
        <div class="photo photo--knight" role="img" aria-label="Photo from the knights and dragon show"></div>
      </div>
      <div class="inside__text">
        <h2 class="inside__lead">Special days all year round</h2>
        <p>Pirate Day, Knights &amp; Dragon show, Wild West, Fairy &amp; Pixie, Prince &amp; Princess, Halloween and Christmas.</p>
        <p>Come and meet our Quillmere Acres characters!</p>
      </div>
    </section>

    <section class="panel panel--inside panel--cafe">
      <div class="band">
        <svg width="412" height="34" viewBox="0 0 412 34" aria-hidden="true"><polygon points="0,8 412,0 412,26 0,34" fill="var(--sky)"/></svg>
        <span class="band__title">Café</span>
      </div>
      <div class="inside__photos" style="height:92px">
        <div class="photo photo--cafe" role="img" aria-label="Photo of the farm café"></div>
      </div>
      <div class="inside__text" style="padding-top:8px">
        <p>Serving hot &amp; cold food and drinks, open all day.</p>
      </div>
      <div class="map" role="img" aria-label="Map showing how to find Quillmere Acres on Ashcombe road"></div>
      <p class="terms">Subject to Terms and Conditions, see our website. All activities are subject to availability and weather.</p>
    </section>
  </div>

</main>
</body>
</html>
```